Construction company yard sign

I would like a design for yard signs for my construction company. It will be used to put outside clients homes as we are working for them and will be used as advertisement for neighbors that are passing by the home.

The sign will be 18x24 and a plastic type material.

Target Market(s)

Homeowners

Font styles to use
Sans Serif

Requirements
Must have
• The most important thing about the sign is the visibility of the lettering and phone number 520-555-0147. The next would be Free roof Inspections. and then I would like to have these 3 words on there as well: Flat - Shingle - Tile

```html
<!DOCTYPE html>
<html lang="en">
<head>
<meta charset="utf-8">
<title>Harlow Construction Group – Yard Sign</title>
<link rel="stylesheet" href="https://fonts.googleapis.com/css2?family=Arimo:wght@400;700&display=swap">
<style>
  :root {
    --band-dark: #1e1214;
    --header-text: #e8b69c;
    --brand-blue: #2e9ad6;
    --sky-top: #f1bb76;
    --sky-mid: #fde27c;
    --roof-red: #8b3b2e;
    --roof-dark: #5a2620;
    --headline: #6a5a22;
    --headline-glow: #f6da2c;
    --call-band: #fde98a;
    --call-text: #1a1112;
  }
  * { margin: 0; padding: 0; box-sizing: border-box; }
  html, body { width: 1200px; height: 900px; overflow: hidden; background: var(--band-dark); }
  .sign {
    position: relative;
    width: 1200px;
    height: 900px;
    font-family: "Arimo", Arial, sans-serif;
    background: var(--band-dark);
  }
  .top-bar {
    position: absolute; left: 0; top: 0; width: 1200px; height: 100px;
    background: var(--band-dark);
  }
  .brand {
    position: absolute; left: 46px; top: 30px;
    display: flex; align-items: center; gap: 10px;
    color: var(--brand-blue);
    font-weight: 700;
    font-size: 21px;
    line-height: 1;
  }
  .brand-mark { width: 30px; height: 30px; background: var(--brand-blue); }
  .brand-name { display: flex; flex-direction: column; gap: 4px; }
  .brand-name .line-two { font-size: 11px; letter-spacing: 3px; }
  .roof-types {
    position: absolute; left: 438px; top: 38px;
    color: var(--header-text);
    font-weight: 700;
    font-size: 38px;
    line-height: 1;
    letter-spacing: 13px;
    white-space: nowrap;
  }
  .hero-photo {
    position: absolute; left: 0; top: 100px; width: 1200px; height: 606px;
    background: linear-gradient(180deg, var(--sky-top) 0%, var(--sky-mid) 35%, var(--sky-mid) 62%, var(--roof-red) 82%, var(--roof-dark) 100%);
  }
  .headline {
    position: absolute; left: 434px; top: 234px;
    color: var(--headline);
    font-weight: 400;
    font-size: 106px;
    line-height: 81px;
    letter-spacing: -6px;
    text-shadow: 4px 3px 0 var(--headline-glow);
  }
  .headline .word-free { letter-spacing: 9px; }
  .headline span { display: block; }
  .call-band {
    position: absolute; left: 0; top: 706px; width: 1200px; height: 120px;
    background: var(--call-band);
    display: flex; align-items: center; justify-content: center;
  }
  .call-text {
    color: var(--call-text);
    font-weight: 700;
    font-size: 114px;
    line-height: 1;
    letter-spacing: -1px;
    white-space: nowrap;
  }
  .bottom-bar {
    position: absolute; left: 0; top: 826px; width: 1200px; height: 74px;
    background: var(--band-dark);
  }
</style>
</head>
<body>
  <div class="sign">
    <header class="top-bar">
      <div class="brand">
        <div class="brand-mark"></div>
        <div class="brand-name">
          <span class="line-one">HARLOW</span>
          <span class="line-two">CONSTRUCTION GROUP</span>
        </div>
      </div>
      <div class="roof-types">Flat - Shingle - Tile</div>
    </header>

    <div class="hero-photo" role="img" aria-label="Photo of red tiled rooftops with brick chimneys and street lamps against a golden sunset sky"></div>

    <h1 class="headline">
      <span class="word-free">FREE</span>
      <span>ROOF</span>
      <span>INSPECTIONS</span>
    </h1>

    <div class="call-band">
      <p class="call-text">CALL: 520-555-0147</p>
    </div>

    <footer class="bottom-bar"></footer>
  </div>
</body>
</html>
```